"Torvela" (spanish restaurant) "Bar de Tapas"

"Torvela" is a spanish restaurant located in the city of Santo Domingo, Dominican Republic. It needs a new and fresh idea for its business card. I would like to take the idea of one of the spaces of the restaurant represented on a business card, for example, the blue and emblematic entrance door of the restaurant, or maybe the bricks on the main room of the restaurant, or how about the bar. Any idea it's good! I invite all the creative designers to participate on the suggestions of it.

What doe sit need? It needs this information on it:

Name: Torvela
Business: Restaurante
Address: Calle Benito Sorel 00, Las Quintas
Phone number: 809-000-0000
website: www.torvelarestaurante.example

Reason: NEED MORE OPTION FOR IT. I WANT YOU TO EXPRESS YOUR DESIGN AS YOU WANT TO NOT AS I ASK YOU TO.

Industry/Entity Type

Restaurant

Contact Information for Business Card

c/Benito Sorel 47

Requirements
Must have
• Creativity. I'm open to new and fresh ideas.
Nice to have
• The entrance door (blue one) would be a plus in the design of the card. Maybe the background could be images of materials like bricks or wood, like the ones in the pictures of the restaurant.

```html
<!DOCTYPE html>
<html lang="es">
<head>
<meta charset="utf-8">
<title>Torvela – Tarjeta de presentación</title>
<link href="https://fonts.googleapis.com/css2?family=Oswald:wght@300;400&display=swap" rel="stylesheet">
<style>
  :root {
    --backdrop: #e9e8e6;
    --gold: #b79d5c;
    --gold-deep: #7a663a;
    --ink: #121010;
    --panel: #1b1718;
    --panel-hi: #2e2729;
  }
  * { margin: 0; padding: 0; box-sizing: border-box; }
  html, body { width: 1200px; height: 800px; overflow: hidden; }
  body {
    background: var(--backdrop);
    position: relative;
    font-family: "Oswald", sans-serif;
  }
  .card {
    position: absolute;
    left: 320px;
    width: 560px;
    height: 320px;
    border-radius: 4px;
    overflow: hidden;
    background: var(--ink);
  }
  .card--front { top: 60px; }
  .card--back { top: 420px; }
  .damask {
    position: absolute;
    inset: 0;
    background:
      radial-gradient(circle at 30% 35%, rgba(183,157,92,.55), transparent 60%),
      radial-gradient(circle at 75% 70%, rgba(183,157,92,.5), transparent 60%),
      linear-gradient(135deg, var(--gold-deep), #3a311d 50%, var(--gold-deep));
  }
  .front-name {
    position: absolute;
    inset: 0;
    display: flex;
    align-items: center;
    justify-content: center;
    font-weight: 400;
    font-size: 58px;
    letter-spacing: 4px;
    text-transform: uppercase;
    color: var(--ink);
    line-height: 1;
  }
  .panel {
    position: absolute;
    left: 24px; top: 20px; right: 24px; bottom: 20px;
    border-radius: 20px;
    display: flex;
    flex-direction: column;
    align-items: center;
    padding-top: 40px;
    background: linear-gradient(160deg, var(--panel-hi), var(--panel) 60%);
    color: var(--gold);
    text-align: center;
  }
  .brand-name {
    font-weight: 400;
    font-size: 56px;
    line-height: 1;
    letter-spacing: 4px;
    text-transform: uppercase;
  }
  .contact {
    list-style: none;
    margin-top: 30px;
    font-weight: 300;
    font-size: 12.5px;
    letter-spacing: 3px;
    line-height: 1;
  }
  .contact li + li { margin-top: 16px; }
  .contact .business,
  .contact .address { text-transform: uppercase; }
  .contact .web { letter-spacing: 2px; }
</style>
</head>
<body>
  <section class="card card--front" aria-label="Anverso de la tarjeta">
    <div class="damask" role="img" aria-label="Patrón ornamental de volutas doradas sobre negro"></div>
    <h1 class="front-name">Torvela</h1>
  </section>

  <section class="card card--back" aria-label="Reverso de la tarjeta">
    <div class="damask" role="img" aria-label="Patrón ornamental de volutas doradas sobre negro"></div>
    <div class="panel">
      <h2 class="brand-name">Torvela</h2>
      <ul class="contact">
        <li class="business">Bar de Tapas · Restaurante</li>
        <li class="address">Benito Sorel 47, Las Quintas</li>
        <li class="phone">809-000-0000</li>
        <li class="web">www.torvelarestaurante.example</li>
      </ul>
    </div>
  </section>
</body>
</html>
```